We need a business card design for a Dubai based company .

We need a business card for a Dubai based company called "Zernova Hookah Supplies Wholesale Co". We mainly import Flavoured Tobacco products and Charcoal which is used for smoking in a Hookah/Shisha and distribute to the wholesalers and retailers. Logo file is attached herewith.

```html
<!DOCTYPE html>
<html lang="en">
<head>
<meta charset="utf-8">
<title>Zernova Hookah Supplies Wholesale Co – Business Card</title>
<link rel="stylesheet" href="https://fonts.googleapis.com/css2?family=Exo+2:wght@400;600&display=swap">
<style>
  :root {
    --backdrop: #b3b3b3;
    --paper: #ffffff;
    --charcoal: #282a2a;
    --crimson: #b93c3f;
    --ink: #2c2c2c;
  }
  * { margin: 0; padding: 0; box-sizing: border-box; }
  html, body { width: 1000px; height: 1200px; overflow: hidden; }
  body {
    background: var(--backdrop);
    position: relative;
    font-family: "Exo 2", "Helvetica Neue", Arial, sans-serif;
  }
  .card {
    position: absolute;
    left: 51px;
    width: 899px;
    height: 540px;
    overflow: hidden;
  }
  .card--front { top: 43px; background: var(--paper); }
  .card--back { top: 617px; background: var(--charcoal); }
  .card__waves { position: absolute; inset: 0; width: 899px; height: 540px; }
  .wordmark {
    position: absolute;
    text-align: center;
    font-weight: 400;
    line-height: 1;
    transform: translate(-50%, -50%);
    white-space: nowrap;
  }
  .wordmark__name {
    display: block;
    font-size: 60px;
    letter-spacing: 9px;
    text-transform: uppercase;
  }
  .wordmark__tagline {
    display: block;
    margin-top: 12px;
    font-size: 12.5px;
    letter-spacing: 4.4px;
    text-transform: uppercase;
  }
  .card--front .wordmark { left: 249px; top: 263px; color: var(--ink); }
  .card--back .wordmark { left: 450px; top: 265px; color: var(--paper); }
  .contact {
    position: absolute;
    left: 507px;
    top: 141px;
    color: var(--ink);
  }
  .contact__name { font-size: 33px; font-weight: 600; line-height: 38px; }
  .contact__role { font-size: 31px; font-weight: 400; line-height: 38px; margin-bottom: 10px; }
  .contact__list { list-style: none; }
  .contact__item {
    display: flex;
    align-items: center;
    height: 44px;
    font-size: 28px;
    letter-spacing: 0.3px;
    white-space: nowrap;
  }
  .contact__icon {
    width: 29px;
    height: 29px;
    margin-right: 10px;
    flex: none;
  }
</style>
</head>
<body>
  <section class="card card--front">
    <svg class="card__waves" viewBox="0 0 899 540" aria-hidden="true">
      <path fill="var(--crimson)" d="M0 0 H899 V65 C820 40 720 15 600 24 C430 36 280 95 140 86 C80 82 30 72 0 65 Z"/>
      <path fill="var(--charcoal)" d="M0 475 C90 505 200 520 300 518 C470 514 620 450 780 456 C830 458 870 465 899 475 V540 H0 Z"/>
    </svg>

    <div class="wordmark">
      <span class="wordmark__name">Zernova</span>
      <span class="wordmark__tagline">Hookah Supplies Wholesale Co</span>
    </div>

    <div class="contact">
      <p class="contact__name">Your Name</p>
      <p class="contact__role">Manager</p>
      <ul class="contact__list">
        <li class="contact__item">
          <svg class="contact__icon" viewBox="0 0 28 28" aria-hidden="true">
            <rect width="28" height="28" rx="3" fill="var(--crimson)"/>
            <path fill="#fff" d="M9 6.5l3 0.5 1.2 4-2 1.5c1 2.2 2.6 3.8 4.3 4.8l1.6-2 4 1.3 0.4 3c-0.3 1.2-1.6 2-3 1.8C12.6 20.6 7.4 15.4 6.6 9.7 6.5 8.2 7.6 6.8 9 6.5z"/>
          </svg>
          123 444 555
        </li>
        <li class="contact__item">
          <svg class="contact__icon" viewBox="0 0 28 28" aria-hidden="true">
            <rect width="28" height="28" rx="3" fill="var(--crimson)"/>
            <path fill="#fff" d="M14 5a6 6 0 0 1 6 6c0 4.5-6 10.5-6 10.5S8 15.5 8 11a6 6 0 0 1 6-6z"/>
            <circle cx="14" cy="11" r="2.3" fill="var(--crimson)"/>
            <rect x="8" y="22.5" width="12" height="1.6" fill="#fff"/>
          </svg>
          789 Your Street Here
        </li>
        <li class="contact__item">
          <svg class="contact__icon" viewBox="0 0 28 28" aria-hidden="true">
            <rect width="28" height="28" rx="3" fill="var(--crimson)"/>
            <rect x="5.5" y="8.5" width="17" height="11" fill="none" stroke="#fff" stroke-width="1.6"/>
            <path d="M5.5 8.5 14 15 22.5 8.5M5.5 19.5 11.5 13.5M22.5 19.5 16.5 13.5" fill="none" stroke="#fff" stroke-width="1.4"/>
          </svg>
          info@yourname.com
        </li>
        <li class="contact__item">
          <svg class="contact__icon" viewBox="0 0 28 28" aria-hidden="true">
            <rect width="28" height="28" rx="3" fill="var(--crimson)"/>
            <g fill="none" stroke="#fff" stroke-width="1.5">
              <circle cx="14" cy="14" r="8"/>
              <ellipse cx="14" cy="14" rx="3.5" ry="8"/>
              <path d="M6 14h16M7.5 10h13M7.5 18h13"/>
            </g>
          </svg>
          www.yourname.com
        </li>
      </ul>
    </div>
  </section>

  <section class="card card--back">
    <div class="wordmark">
      <span class="wordmark__name">Zernova</span>
      <span class="wordmark__tagline">Hookah Supplies Wholesale Co</span>
    </div>
  </section>
</body>
</html>
```